Business card with professional look

I would like a creative yet professional looking business card for our business. We sell broadcast TV related security products for mobile phones, set top boxes, and tablets. Our customers are international. We have a logo we like and I would like to possibly add some color to the business card but keep it professional looking.

Target Market(s)

Professionals in the TV, cable, ans Satellite industries

Industry/Entity Type

Cable Tv

Contact Information for Business Card

Name Ned Vastermill, title CEO, Address 8130 Harborline Court, Suite 400, Del Arvo, CA 91584 USA, phone numbers m:+1.619.284.7302 o:+1.855.672.9140, email, logo

Font styles to use
Other font styles liked:
• Open to any font that looks good with logo

Requirements
Must have
• professional look with colors coordinated with logo colors. would like to add one or two different colors as well as some form of background color

```html
<!DOCTYPE html>
<html lang="en">
<head>
<meta charset="utf-8">
<title>Vaultcast – Business Card</title>
<link rel="stylesheet" href="https://fonts.googleapis.com/css2?family=Lato:wght@400;700;900&display=swap">
<style>
  :root {
    --page-bg: #e6e7e9;
    --card-bg: #f7f7f6;
    --ink: #4a4b4d;
    --ink-soft: #5a5b5e;
    --brand-blue: #2a8fd0;
    --brand-blue-light: #5fb0e3;
    --band-grey: #464749;
    --band-text: #ffffff;
  }
  * { box-sizing: border-box; margin: 0; padding: 0; }
  html, body {
    width: 1200px;
    height: 800px;
    overflow: hidden;
    background: var(--page-bg);
    font-family: "Lato", Arial, sans-serif;
  }
  .stage {
    width: 1200px;
    height: 800px;
    display: flex;
    align-items: center;
    justify-content: center;
  }
  .business-card {
    position: relative;
    width: 910px;
    height: 520px;
    background: var(--card-bg);
    border-radius: 34px;
    overflow: hidden;
    box-shadow: 0 6px 24px rgba(0,0,0,0.12);
  }
  .identity {
    position: absolute;
    left: 92px;
    top: 112px;
  }
  .person-name {
    font-size: 38px;
    font-weight: 900;
    color: var(--ink);
    letter-spacing: 0.5px;
    line-height: 1.1;
  }
  .person-name .first-name { color: var(--brand-blue); }
  .person-title {
    font-size: 30px;
    font-weight: 700;
    color: var(--ink);
    line-height: 1.15;
  }
  .phones {
    position: absolute;
    left: 92px;
    top: 276px;
    font-size: 24px;
    color: var(--ink-soft);
    line-height: 1.45;
  }
  .brand {
    position: absolute;
    left: 500px;
    top: 150px;
    display: flex;
    align-items: center;
    gap: 14px;
  }
  .brand-mark {
    width: 46px;
    height: 46px;
    background: var(--brand-blue);
  }
  .brand-name {
    font-size: 60px;
    font-weight: 900;
    color: var(--ink);
    letter-spacing: -1px;
  }
  .web-contact {
    position: absolute;
    left: 500px;
    top: 296px;
    font-size: 24px;
    color: var(--ink-soft);
    line-height: 1.45;
  }
  .accent-block {
    position: absolute;
    left: 0;
    width: 92px;
    background: var(--brand-blue);
  }
  .accent-block.upper {
    bottom: 62px;
    height: 56px;
    width: 46px;
    background: var(--brand-blue-light);
  }
  .accent-block.lower {
    bottom: 0;
    height: 62px;
  }
  .address-band {
    position: absolute;
    left: 92px;
    right: 0;
    bottom: 0;
    height: 62px;
    background: var(--band-grey);
    color: var(--band-text);
    font-size: 23px;
    display: flex;
    align-items: center;
    padding-left: 28px;
    letter-spacing: 0.3px;
  }
</style>
</head>
<body>
<main class="stage">
  <article class="business-card">
    <div class="identity">
      <p class="person-name"><span class="first-name">Ned</span> Vastermill</p>
      <p class="person-title">CEO</p>
    </div>

    <div class="phones">
      <p class="phone office">Office +1.855.672.9140</p>
      <p class="phone mobile">Mobile +1.619.284.7302</p>
    </div>

    <div class="brand">
      <span class="brand-name">Vaultcast</span>
      <span class="brand-mark"></span>
    </div>

    <div class="web-contact">
      <p class="email">youremailaddress@email.com</p>
      <p class="website">www.yourwebsite.com</p>
    </div>

    <div class="accent-block upper"></div>
    <div class="accent-block lower"></div>
    <div class="address-band">8130 Harborline Court, Suite 400, Del Arvo, CA 91584 USA</div>
  </article>
</main>
</body>
</html>
```